Web Design Project

Brightwater Digital owns and operates a large number of editorial websites. These websites provides mostly consumers in the financial services space with information and price comparisons for a particular service.

Brightwater Digital, as the holding company for each of these sites, currently has no website. We need to build a website targeted towards potential partners for our websites. The idea being that when we start a conversation with a partner, they can view our site and obtain some basic information about who we are.

The structure of the site is to be very simple, containing only a brief description about who we are, our contact details and a list of some of our websites:
• CoverQuest.net.au
• AutoPolicyMatcher.com.au
• NestPolicyMatcher.com.au
• WellPolicyMatcher.com.au
• CoverQuestMatcher.com.au
• TripPolicyMatcher.com.au
• CritterPolicyMatcher.com.au
• CashAdvanceMatcher.com.au
• MobileCoolingUnit.com.au
• FixedSaverYields.com.au
• ThriftyHabits.com.au
• PurseGran.com.au
• TameThePlastic.com.au
• PurseMinder.com.au
• ThirdPartyClaimsCoverOzland.com.au
• Trade-Protect.com.au
• AutoPolicyProviders.com.au
• WellPolicyProviders.com.au
• NestPolicyOzland.com
• CoverQuestOzland.com
• WageShieldPolicyOzland.com
• WellPolicyOzland.com
• CritterPolicyOzland.com
• CashAdvancesOzland.com
• PlasticPaysOzland.com
• NestLendersOzland.com
• NestEggFunds.net.au

The design of the site should say 'Internet company', 'professional', 'fresh thinking'. The design should not look like a corporate site that you would see from any corporate services business with images of people in suits. We are ultimately an Internet business and there should be a unique feel to the site.

We are open to a suggestion of a colour pallet as the holding company does not have an established logo.

Some sites that we like are:

http://www.prismwork-studio.co.uk/#home
http://sample00.layoutvault.example/wt_48248/index.html
http://sample00.layoutvault.example/wordpress_46388/
http://mindvolt.example/
http://www.tandora.us/
http://www.kelvorabintu.example/
http://www.slickfrontpages.example/Corporate/design-ideas-detail.html?id=7916
http://trebla.example/
http://orvantek.example/

Reason: Hi all, Apologies, but I need to extend the timeline. One of our key stakeholders is away for the next week. There are a few good designs that we have received to date and there are some tweaks that we would like to see before making a final decision. Thank you to everyone that has submitted designs - Have a great new year. Derek

Reason: Sorry to have to delay the deadline on this, but we did not find anything in the designs really resonated with us. We will have a further think about the existing designs that have been submitted and how we can provide more specific feedback to the designers to make some modifications to the designs.

Target Market(s)

We are targeting insurance companies / brokers that we are talking to. The idea is that we show a professional face to them.

Industry/Entity Type

Financial

Requirements
Must have
• Home Page (possibly integrated with About us details)
Contact Us
Our Sites

```html
<!DOCTYPE html>
<html lang="en">
<head>
<meta charset="utf-8">
<title>Brightwater Digital</title>
<link rel="stylesheet" href="https://fonts.googleapis.com/css2?family=Comfortaa:wght@400;700&family=Lobster&family=PT+Sans:wght@400;700&display=swap">
<style>
:root{
  --bar-blue:#00b3e6;
  --title-blue:#0f6fae;
  --ink:#111111;
  --field-fill:#cdf5fd;
  --field-edge:#7fcfe3;
  --footer-aqua:#9ff3fd;
  --divider:#7fdcf2;
  --white:#ffffff;
}
*{box-sizing:border-box;margin:0;padding:0}
html,body{width:1058px;height:1200px;overflow:hidden;background:var(--white)}
body{position:relative;font-family:"PT Sans",Tahoma,sans-serif;color:var(--ink)}

.top-bar{position:absolute;left:0;top:0;width:1058px;height:69px;background:var(--bar-blue);color:var(--white)}
.top-bar__phone{position:absolute;left:46px;top:25px;font-size:15px}
.main-nav{position:absolute;right:30px;top:22px;display:flex;gap:45px;font-family:"Comfortaa",sans-serif;font-size:17px}
.main-nav a{color:var(--white);text-decoration:none}

.hero{position:absolute;left:0;top:69px;width:1058px;height:419px;overflow:hidden}
.hero__art{position:absolute;inset:0;background:
  radial-gradient(circle at 12% 78%,#f04a2a 0,#f6c21a 12%,rgba(246,194,26,0) 24%),
  radial-gradient(circle at 82% 55%,#a9dff5 0,#6fc6ec 25%,rgba(111,198,236,0) 45%),
  linear-gradient(180deg,#6fd8f7 0%,#3fcff3 55%,#8ae6f9 100%)}
.hero__title{position:absolute;left:0;width:936px;top:62px;text-align:center;font-family:"Lobster",cursive;font-size:50px;color:var(--title-blue)}
.hero__caption{position:absolute;left:0;top:343px;width:1058px;height:76px;background:rgba(140,238,252,.75);text-align:center;line-height:76px;font-size:20px}

.welcome{position:absolute;left:0;top:500px;width:1058px;text-align:center}
.welcome__heading{font-family:"Lobster",cursive;font-weight:400;font-size:27px;color:var(--title-blue);line-height:40px}
.welcome__text{width:940px;margin:4px auto 0;font-size:13.5px;line-height:27px}
.section-rule{position:absolute;left:90px;top:642px;width:860px;height:1px;background:linear-gradient(90deg,rgba(127,220,242,0),var(--divider) 50%,rgba(127,220,242,0))}

.map{position:absolute;left:48px;top:686px;width:247px;height:240px;border:1px solid var(--field-edge);background:linear-gradient(135deg,#e9e7e2,#dcdad4)}
.address{position:absolute;left:320px;top:684px;font-size:16px;line-height:40px;font-style:normal}
.column-rule{position:absolute;left:609px;top:668px;width:1px;height:258px;background:linear-gradient(180deg,rgba(127,220,242,0),var(--divider) 50%,rgba(127,220,242,0))}

.contact-form .field{position:absolute;left:669px;width:291px;height:45px;border:1px solid var(--field-edge);border-radius:9px;background:var(--field-fill);padding:10px 0 0 25px;font-size:14.5px;color:#334a55}
.contact-form .field--comments{height:112px}
.send-button{position:absolute;left:842px;top:1062px;width:117px;height:38px;border:1px solid var(--field-edge);border-radius:8px;background:linear-gradient(180deg,#eafcff 0%,#bff0fb 45%,#52d3ef 60%,#bdf0fa 100%);font-size:15px;text-align:center;line-height:36px}

.site-footer{position:absolute;left:0;top:1123px;width:1058px;height:77px;background:var(--footer-aqua)}
.footer-nav{position:absolute;left:46px;top:17px;font-family:"Comfortaa",sans-serif;font-size:17px}
.footer-nav a{color:var(--ink);text-decoration:none}
.social{position:absolute;left:832px;top:23px}
</style>
</head>
<body>
<header class="top-bar">
  <div class="top-bar__phone">Call : 02 7415 3068</div>
  <nav class="main-nav"><a href="#">About Us</a><a href="#">Case Studies</a><a href="#">Blog</a><a href="#">Contact Us</a></nav>
</header>

<section class="hero">
  <div class="hero__art" role="img" aria-label="Colourful abstract swirls beside pale blue city towers"></div>
  <h1 class="hero__title">Brightwater Digital</h1>
  <p class="hero__caption">If you are interested in partnering with us on one or multiple of our sites, please contact us.</p>
</section>

<section class="welcome">
  <h2 class="welcome__heading">Welcome</h2>
  <p class="welcome__text">Brightwater Digital is an Australian-based internet marketing company.&nbsp; We specialise in attracting customers from our directory of more than 100 sites to our network of trusted partners.&nbsp; Our skill lies in generating targeted traffic to our range of websites and identifying the right partners for each of the sites, ensuring that the visitors to our sites get what they are looking for.</p>
</section>
<div class="section-rule"></div>

<div class="map" role="img" aria-label="Street map showing the office location"></div>
<address class="address">
  Brightwater Digital Pty Ltd<br>
  Suite 412<br>
  18 Harbourline Street<br>
  Coralbay Junction NSW&nbsp;&nbsp; 2099<br>
  Tel: 02 7415 3068<br>
  Email: hello@brightwaterdigital.example
</address>
<div class="column-rule"></div>

<form class="contact-form">
  <div class="field" style="top:673px">Name</div>
  <div class="field" style="top:731px">Email</div>
  <div class="field" style="top:794px">Mobile</div>
  <div class="field" style="top:855px">Company</div>
  <div class="field field--comments" style="top:915px">Comments</div>
  <div class="send-button">Send</div>
</form>

<footer class="site-footer">
  <nav class="footer-nav"><a href="#">About Us</a> | <a href="#">Case Studies</a> | <a href="#">Blog</a> | <a href="#">Contact Us</a></nav>
  <svg class="social" width="150" height="36" viewBox="0 0 150 36" role="img" aria-label="Social links">
    <g fill="#8fb4c8" stroke="#6f93a6" stroke-width="1.5">
      <circle cx="18" cy="18" r="15"/>
      <circle cx="55" cy="18" r="15"/>
      <circle cx="92" cy="18" r="15"/>
      <circle cx="129" cy="18" r="15"/>
    </g>
  </svg>
</footer>
</body>
</html>
```